Business card design for Birch Engineering Torvant

We need a new business card design along with all the necessary to place an order. The company is Birch Engineering Torvant and we recently updated our logo.

```html
<!DOCTYPE html>
<html lang="en">
<head>
<meta charset="UTF-8">
<title>Birch Engineering Torvant — Business Card</title>
<link href="https://fonts.googleapis.com/css2?family=Montserrat:wght@400;500;700&display=swap" rel="stylesheet">
<style>
  :root {
    --page: #ffffff;
    --card: #1b1b1b;
    --grey: #9a9994;
    --yellow: #e4c500;
  }
  * { margin: 0; padding: 0; box-sizing: border-box; }
  html, body {
    width: 1200px; height: 1200px; overflow: hidden;
    background: var(--page);
    font-family: "Montserrat", sans-serif;
  }
  .canvas { position: relative; width: 1200px; height: 1200px; }
  .card {
    position: absolute; left: 181px; width: 845px; height: 483px;
    background: var(--card);
  }
  .card--front { top: 94px; }
  .card--back { top: 631px; }

  .brand {
    position: absolute; display: flex; align-items: center;
    color: var(--grey); font-weight: 700; letter-spacing: 0.08em; white-space: nowrap;
  }
  .brand__mark { background: var(--yellow); flex: none; }
  .card--front .brand {
    left: 50%; top: 50%; transform: translate(-50%, -50%);
    font-size: 24px; gap: 16px;
  }
  .card--front .brand__mark { width: 26px; height: 26px; }
  .card--back .brand {
    left: 61px; top: 260px; font-size: 17px; gap: 12px;
  }
  .card--back .brand__mark { width: 18px; height: 18px; background: var(--grey); }

  .front__web {
    position: absolute; right: 51px; bottom: 40px;
    color: var(--yellow); font-size: 17px; font-weight: 500;
  }

  .contact { position: absolute; left: 475px; top: 116px; color: var(--grey); }
  .contact__name { font-size: 31px; font-weight: 700; letter-spacing: 0.12em; line-height: 1; }
  .contact__title { font-size: 20px; font-weight: 700; margin-top: 6px; }
  .contact__address { font-size: 19px; font-weight: 400; margin-top: 16px; }
  .contact__list { list-style: none; margin-top: 22px; }
  .contact__item {
    display: flex; align-items: center; gap: 19px;
    height: 32px; margin-bottom: 8.5px;
    font-size: 20px; font-weight: 500; letter-spacing: 0.04em;
  }
  .contact__icon { width: 32px; height: 32px; flex: none; }
</style>
</head>
<body>
<div class="canvas">
  <section class="card card--front">
    <div class="brand"><span class="brand__mark"></span>BIRCH ENGINEERING TORVANT</div>
    <p class="front__web">www.yourwebsite.com</p>
  </section>

  <section class="card card--back">
    <div class="brand"><span class="brand__mark"></span>BIRCH ENGINEERING TORVANT</div>
    <div class="contact">
      <h1 class="contact__name">Your Name</h1>
      <p class="contact__title">Your Title</p>
      <p class="contact__address">Your Address and Country</p>
      <ul class="contact__list">
        <li class="contact__item">
          <svg class="contact__icon" viewBox="0 0 32 32" aria-hidden="true">
            <circle cx="16" cy="16" r="16" fill="var(--grey)"/>
            <path d="M10 9 l3 -1 2 4 -2 2 q2 4 5 5 l2 -2 4 2 -1 3 q-3 2 -9 -3 q-5 -5 -4 -10z" fill="var(--card)"/>
          </svg>
          123-456-789
        </li>
        <li class="contact__item">
          <svg class="contact__icon" viewBox="0 0 32 32" aria-hidden="true">
            <circle cx="16" cy="16" r="16" fill="var(--grey)"/>
            <g fill="none" stroke="var(--card)" stroke-width="1.3">
              <circle cx="16" cy="16" r="8"/>
              <ellipse cx="16" cy="16" rx="3.5" ry="8"/>
              <path d="M8 16h16M9.5 12h13M9.5 20h13"/>
            </g>
          </svg>
          www.yourwebsite.com
        </li>
        <li class="contact__item">
          <svg class="contact__icon" viewBox="0 0 32 32" aria-hidden="true">
            <circle cx="16" cy="16" r="16" fill="var(--grey)"/>
            <g fill="none" stroke="var(--card)" stroke-width="1.4">
              <rect x="8" y="11" width="16" height="10"/>
              <path d="M8 11l8 6 8-6M8 21l6-5M24 21l-6-5"/>
            </g>
          </svg>
          email@info.com
        </li>
      </ul>
    </div>
  </section>
</div>
</body>
</html>
```